Website Page Re-Design

I have 2 pages that need to be re-designed on my site. This is the site so you can take a look and get a feel for the layout etc, www.vortaplay.com
I have included screen shots of the individual pages I want redone as well as some examples from other sites for ideas.

Homepage Story, would like the redo sunday file, to be made stunning, only the content, picture and share buttons need be altered the, would like and emphasis on intergrating the share buttons, the story page starts here http://www.vortaplay.com/league/ball-hockey/mens/news-division/ so what is beingcreated is when the read more is clicked

Free Agent Forms:
Needs to be re-worked so that there isn't so much white space on the page.

Industry/Entity Type

News

Requirements
Must have
• share buttons to slick very well intergrated
Nice to have
• Share buttons to be top notch

```html
<!DOCTYPE html>
<html lang="en">
<head>
<meta charset="utf-8">
<title>Vortaplay – News</title>
<link rel="stylesheet" href="https://fonts.googleapis.com/css2?family=Montserrat:wght@700;800&family=Arimo:wght@400;700&family=Oswald:wght@500;600&family=Open+Sans:ital,wght@1,400;1,600&family=Cousine:wght@400&display=swap">
<style>
:root{
  --bg-green:#7db640;
  --bg-green-light:#9fcb63;
  --panel:#e6f2d6;
  --card:#ffffff;
  --card-edge:#d9e3cc;
  --title:#1d3407;
  --body:#2b2b2b;
  --date:#5e9524;
  --nav-yellow:#f7df63;
  --nav-ink:#1b1b1b;
  --bar-black:#141414;
  --share-col:#eceef0;
  --fb:#3b5998;
  --tw:#32a8dc;
  --pin:#cc2127;
  --footer:#f2f8e8;
}
*{box-sizing:border-box;margin:0;padding:0}
html,body{width:1200px;height:1078px;overflow:hidden}
body{
  position:relative;
  background:radial-gradient(ellipse at 50% 40%,var(--bg-green-light) 0%,var(--bg-green) 60%);
  font-family:"Arimo",Arial,sans-serif;
}
.brand{
  position:absolute;left:132px;top:24px;
  font-family:"Montserrat",sans-serif;font-weight:800;font-size:44px;
  color:#ffffff;letter-spacing:-1px;
}
.top-nav{
  position:absolute;left:658px;top:0;width:410px;height:27px;
  background:var(--nav-yellow);border-radius:0 0 8px 8px;
  display:flex;align-items:center;justify-content:space-around;
}
.top-nav a{font:700 15px "Arimo",sans-serif;color:var(--nav-ink);text-decoration:none;padding:0 10px;border-right:1px solid #b39b2b}
.top-nav a:last-child{border-right:none}
.main-nav{
  position:absolute;left:514px;top:42px;width:554px;height:46px;
  background:var(--bar-black);border-radius:4px 10px 6px 12px;
  display:flex;align-items:center;justify-content:center;gap:6px;
}
.main-nav a{font:italic 600 15px "Open Sans",sans-serif;color:#fff;text-decoration:underline;padding:0 9px;border-right:1px solid #666}
.main-nav a:last-child{border-right:none}
.page{
  position:absolute;left:132px;top:104px;width:936px;height:910px;
  background:var(--panel);border-radius:8px;
}
.banner{
  position:absolute;left:16px;top:12px;width:907px;height:108px;
  background:linear-gradient(180deg,#84bb45,#4f8a1c);border-radius:4px;
}
.banner-players{
  position:absolute;left:14px;top:-10px;width:570px;height:118px;
  background:linear-gradient(90deg,#b9584c,#d9b29b 30%,#c9433a 60%,#b8b2ad);
}
.social-follow{
  position:absolute;left:694px;top:22px;width:165px;height:64px;
  background:#0c0c0c;border-radius:5px;
  display:flex;align-items:center;gap:12px;padding-left:14px;
}
.social-follow .mark{width:30px;height:30px;background:#5b7bbf;border-radius:3px}
.social-follow span{font:italic 400 16px/1.05 "Open Sans",sans-serif;color:#fff}
.post{
  position:absolute;left:14px;width:909px;height:364px;
  background:var(--card);border:1px solid var(--card-edge);
}
.post-photo{position:absolute;left:8px;top:8px;width:512px;height:346px;background:linear-gradient(160deg,#e6e2da 0%,#3b5fb0 45%,#e8e8ea 65%,#2f7d32 100%);border:1px solid #bbb}
.post-body{position:absolute;left:547px;top:10px;width:250px}
.post-date{
  display:inline-block;background:var(--date);color:#fff;
  font:600 15px/22px "Oswald",sans-serif;padding:0 18px 0 16px;
  clip-path:polygon(0 0,100% 0,93% 50%,100% 100%,0 100%,7% 50%);
}
.post-title{margin-top:14px;font:700 33px/1.02 "Montserrat",sans-serif;color:var(--title)}
.post-text{margin-top:14px;font:13.4px/18.6px "Arimo",sans-serif;color:var(--body)}
.post-text p+p{margin-top:6px}
.read-more{
  display:inline-block;margin-top:12px;background:#e2e2e2;
  font:500 13px/22px "Oswald",sans-serif;color:#222;padding:0 10px;
}
.share-rail{
  position:absolute;left:818px;top:0;width:86px;height:362px;background:var(--share-col);
  padding:14px 0 0 10px;
}
.share-rail::before{content:"";position:absolute;left:-14px;top:28px;border:14px solid transparent;border-right-color:var(--share-col);border-left:none}
.share-item{height:68.4px}
.share-count{width:56px;height:38px;background:#fff;border:1px solid #d4d7da;border-radius:3px;font:17px/36px "Cousine",monospace;text-align:center;color:#111}
.share-btn{margin-top:5px;width:56px;height:20px;border-radius:2px;font:700 10px/20px "Arimo",sans-serif;color:#fff;display:flex;align-items:center;gap:4px;padding-left:4px}
.share-btn i{width:10px;height:10px;background:rgba(255,255,255,.85);display:inline-block}
.btn-fb{background:var(--fb)}
.btn-tw{background:var(--tw)}
.btn-in{background:#fff;color:#333;border:1px solid #bbb}.btn-in i{background:#0e76a8}
.btn-pin{background:var(--pin)}
.btn-blog{background:#fff;color:#333;border:1px solid #bbb}.btn-blog i{background:#f57d00}
.footer{position:absolute;left:132px;top:1048px;font:11px "Arimo",sans-serif;letter-spacing:1.5px;color:var(--footer)}
</style>
</head>
<body>
<div class="brand">Vortaplay</div>
<nav class="top-nav"><a>Home</a><a>About Us</a><a>FAQS</a><a>Contact Us</a><a>Jobs</a></nav>
<nav class="main-nav"><a>Leagues</a><a>Schedules &amp; More</a><a>Register</a><a>Pay</a><a>Forum</a><a>Sponsors</a></nav>

<main class="page">
  <div class="banner">
    <div class="banner-players" role="img" aria-label="Row of league players in team jerseys"></div>
    <div class="social-follow"><div class="mark"></div><span>Find Us On<br>Friendbook</span></div>
  </div>

  <article class="post" style="top:138px">
    <div class="post-photo" role="img" aria-label="Team in white shirts posing with a large charity cheque"></div>
    <div class="post-body">
      <div class="post-date">07 JUL 2013</div>
      <h2 class="post-title">Lorem ipsum dolor sit amet</h2>
      <div class="post-text">
        <p>Lorem ipsum dolor sit amet, consectetur adipisicing elit, sed do eiusmod tempor incididunt ut labore et dolore magna aliqua. Ut enim ad minim veniam, quis nostrud exercitation ullamco laboris nisi ut aliquip ex ea commodo consequat.</p>
        <p>Duis aute irure dolor in reprehenderit in voluptate velit esse cillum dolore eu fugiat nulla pariatur. Excepteur sint occaecat cupidatat non proident.</p>
      </div>
      <span class="read-more">READ MORE</span>
    </div>
    <aside class="share-rail">
      <div class="share-item"><div class="share-count">3511</div><div class="share-btn btn-fb"><i></i>Share</div></div>
      <div class="share-item"><div class="share-count">1228</div><div class="share-btn btn-tw"><i></i>Post</div></div>
      <div class="share-item"><div class="share-count">519</div><div class="share-btn btn-in"><i></i>Share</div></div>
      <div class="share-item"><div class="share-count">621</div><div class="share-btn btn-pin"><i></i>Pinboard</div></div>
      <div class="share-item"><div class="share-count">81</div><div class="share-btn btn-blog"><i></i>Blogspace</div></div>
    </aside>
  </article>

  <article class="post" style="top:530px">
    <div class="post-photo" role="img" aria-label="Team in white shirts posing with a large charity cheque"></div>
    <div class="post-body">
      <div class="post-date">07 JUL 2013</div>
      <h2 class="post-title">Lorem ipsum dolor sit amet</h2>
      <div class="post-text">
        <p>Lorem ipsum dolor sit amet, consectetur adipisicing elit, sed do eiusmod tempor incididunt ut labore et dolore magna aliqua. Ut enim ad minim veniam, quis nostrud exercitation ullamco laboris nisi ut aliquip ex ea commodo consequat.</p>
        <p>Duis aute irure dolor in reprehenderit in voluptate velit esse cillum dolore eu fugiat nulla pariatur. Excepteur sint occaecat cupidatat non proident.</p>
      </div>
      <span class="read-more">READ MORE</span>
    </div>
    <aside class="share-rail">
      <div class="share-item"><div class="share-count">3511</div><div class="share-btn btn-fb"><i></i>Share</div></div>
      <div class="share-item"><div class="share-count">1228</div><div class="share-btn btn-tw"><i></i>Post</div></div>
      <div class="share-item"><div class="share-count">519</div><div class="share-btn btn-in"><i></i>Share</div></div>
      <div class="share-item"><div class="share-count">621</div><div class="share-btn btn-pin"><i></i>Pinboard</div></div>
      <div class="share-item"><div class="share-count">81</div><div class="share-btn btn-blog"><i></i>Blogspace</div></div>
    </aside>
  </article>
</main>

<footer class="footer">© 2011, VORTAPLAY. ALL RIGHTS RESERVED.</footer>
</body>
</html>
```